Health and wellnes company needs business cards

We are a Health and wellness business just relocated to Spain. Here nobody knows our business so we would like to put some of our services on the card. Clean design with logo.

Contact Information for Business Card

Brightmeadow
Clara & Tobias Wennberg
Calle de los Almendros 17
Puerto de Valmira
Mobile: 0046 731 402768
info@brightmeadow-example.se

Font styles to use
Serif

Colors
85cae6
85acd3
b768aa

Requirements
Must have
• these Services somewhere on the card
• - Private or group yoga
• - Reconnective healing
• - Kitesurfing lessons
• - Massage
• LOgo somewhere
Nice to have
• Colours that go with the logo please

```html
<!DOCTYPE html>
<html lang="en">
<head>
<meta charset="utf-8">
<title>Brightmeadow business cards</title>
<link rel="stylesheet" href="https://fonts.googleapis.com/css2?family=Roboto:wght@400;500;700&display=swap">
<style>
  :root {
    --navy: #1b365f;
    --teal: #6cc3c4;
    --paper: #f7f8fb;
    --ink: #555a60;
    --white: #f4f4f6;
    --backdrop: #b8b8b8;
  }
  * { margin: 0; padding: 0; box-sizing: border-box; }
  html, body {
    width: 1172px; height: 1200px; overflow: hidden;
    background: var(--backdrop);
    font-family: "Roboto", Arial, sans-serif;
  }
  .canvas { position: relative; width: 1172px; height: 1200px; }
  .card { position: absolute; left: 214px; width: 744px; height: 428px; }
  .card--front { top: 122px; background: var(--navy); }
  .card--back { top: 645px; background: var(--paper); }

  .brand-dot { position: absolute; border-radius: 50%; background: var(--teal); }
  .card--front .brand-dot { width: 110px; height: 110px; left: 317px; top: 110px; }
  .card--back .brand-dot { width: 86px; height: 86px; left: 103px; top: 40px; }

  .wordmark {
    position: absolute; font-weight: 500; text-transform: uppercase;
    letter-spacing: 1px; line-height: 1; white-space: nowrap;
  }
  .card--front .wordmark {
    left: 0; width: 100%; text-align: center; top: 262px;
    font-size: 44px; color: var(--white);
  }
  .card--back .wordmark {
    left: 26px; top: 151px; font-size: 30px; color: var(--navy);
  }

  .website {
    position: absolute; left: 0; width: 100%; top: 362px; text-align: center;
    font-size: 22px; letter-spacing: 2.5px; color: var(--white);
  }
  .website .accent { color: var(--teal); }

  .person { position: absolute; left: 26px; top: 252px; }
  .person__name { font-size: 28px; font-weight: 700; color: var(--navy); letter-spacing: -0.3px; }
  .person__role { font-size: 21px; color: var(--teal); margin-top: 4px; }

  .contact { position: absolute; left: 26px; top: 347px; list-style: none; }
  .contact li {
    display: flex; align-items: center; gap: 10px;
    font-size: 21px; color: var(--ink); height: 28px;
  }
  .contact svg { width: 17px; height: 17px; flex: none; }

  .details { position: absolute; left: 484px; top: 150px; }
  .details__heading { font-size: 22px; font-weight: 700; color: var(--navy); }
  .details__address { font-size: 21px; color: var(--ink); line-height: 29px; margin-top: 6px; }
  .details__heading--services { margin-top: 10px; }
  .services { list-style: none; margin-top: 6px; }
  .services li {
    position: relative; padding-left: 23px;
    font-size: 21px; color: var(--ink); line-height: 28.5px;
  }
  .services li::before {
    content: ""; position: absolute; left: 1px; top: 10px;
    width: 9px; height: 9px; border-radius: 50%; background: var(--navy);
  }
</style>
</head>
<body>
<main class="canvas">
  <section class="card card--front" aria-label="Card front">
    <span class="brand-dot"></span>
    <h1 class="wordmark">Brightmeadow</h1>
    <p class="website"><span class="accent">www.</span>brightmeadow<span class="accent">.com</span></p>
  </section>

  <section class="card card--back" aria-label="Card back">
    <span class="brand-dot"></span>
    <h2 class="wordmark">Brightmeadow</h2>

    <div class="person">
      <p class="person__name">Clara &amp; Tobias Wennberg</p>
      <p class="person__role">Co-Founder</p>
    </div>

    <ul class="contact">
      <li>
        <svg viewBox="0 0 24 24" aria-hidden="true"><path fill="#1b365f" d="M6.6 10.8a15 15 0 0 0 6.6 6.6l2.2-2.2c.3-.3.7-.4 1-.2 1.1.4 2.3.6 3.6.6.6 0 1 .4 1 1V20c0 .6-.4 1-1 1A17 17 0 0 1 3 4c0-.6.4-1 1-1h3.5c.6 0 1 .4 1 1 0 1.3.2 2.5.6 3.6.1.3 0 .7-.2 1z"/><path fill="none" stroke="#1b365f" stroke-width="1.8" d="M14 3.5a7 7 0 0 1 6.5 6.5M14 7a3.5 3.5 0 0 1 3 3"/></svg>
        0046 731 402768
      </li>
      <li>
        <svg viewBox="0 0 24 24" aria-hidden="true"><rect x="2" y="5" width="20" height="14" fill="#1b365f"/><path d="M3 6l9 7 9-7M3 18l7-6M21 18l-7-6" fill="none" stroke="#f7f8fb" stroke-width="1.4"/></svg>
        info@brightmeadow-example.se
      </li>
    </ul>

    <div class="details">
      <h3 class="details__heading">Address</h3>
      <p class="details__address">Calle de los Almendros 17<br>Puerto de Valmira</p>
      <h3 class="details__heading details__heading--services">Services</h3>
      <ul class="services">
        <li>Private or group yoga</li>
        <li>Reconnective healing</li>
        <li>Kitesurfing lessons</li>
        <li>Massage</li>
      </ul>
    </div>
  </section>
</main>
</body>
</html>
```